Banner  (Schriftart: Museo Sans rounded)
Banner (Schriftart: Museo Sans rounded)
Zielgruppe
Eltern, Gäste und Personen am Fußballplatz, die über einen Immobilienverkauf nachdenken
Aufgabenstellung
Raumglück – Die Immobilienmakler ist ein Immobilienmakler-Unternehmen. Der Banner (6 m × 0,75 m) soll am Fußballplatz Personen ansprechen, die über einen Immobilienverkauf nachdenken. Das Design soll das Firmenlogo, eine Personenabbildung des Inhabers sowie ein ansprechendes, werbewirksames Layout enthalten. Die Umsetzung und Wirkung liegt im kreativen Ermessen der Designer.

```html
<!DOCTYPE html>
<html lang="de">
<head>
<meta charset="utf-8">
<title>Raumglück – Bandenbanner</title>
<link rel="stylesheet" href="https://fonts.googleapis.com/css2?family=Nunito:wght@400;600;900&display=swap">
<style>
  :root {
    --canvas-grey: #d3d1d5;
    --banner-white: #ffffff;
    --brand-lilac: #a89bbf;
    --brand-lilac-dark: #7d6f99;
    --brand-ink: #2b2633;
    --photo-suit: #5c5470;
    --photo-house: #b7adc9;
  }
  * { margin: 0; padding: 0; box-sizing: border-box; }
  html, body { width: 1000px; height: 1200px; overflow: hidden; background: var(--canvas-grey); }
  body { font-family: "Nunito", sans-serif; position: relative; }

  .banner {
    position: absolute; left: 26px; top: 824px;
    width: 948px; height: 118px;
    background: var(--banner-white);
    overflow: hidden;
  }
  .banner-band { position: absolute; inset: 0; }

  .brand {
    position: absolute; left: 36px; top: 38px;
    display: flex; align-items: center; gap: 8px;
  }
  .brand-dot { width: 16px; height: 16px; border-radius: 50%; background: var(--brand-lilac); flex: none; }
  .brand-name {
    font-weight: 900; font-size: 15px; line-height: 16px; letter-spacing: 0.3px;
    color: var(--brand-ink);
  }

  .headline {
    position: absolute; top: 12px;
    font-weight: 900; font-size: 46px; line-height: 1; letter-spacing: -0.5px;
  }
  .headline-object { left: 158px; color: var(--brand-lilac); }
  .headline-action { left: 408px; color: var(--banner-white); }

  .promise {
    position: absolute; left: 159px; top: 67px;
    font-weight: 400; font-size: 22px; line-height: 21px; letter-spacing: 2.4px;
    color: var(--brand-lilac-dark);
  }

  .contact {
    position: absolute; left: 413px; top: 65px;
    list-style: none; color: var(--banner-white);
    font-weight: 600; font-size: 15px; line-height: 1;
  }
  .contact li { display: flex; align-items: center; gap: 7px; height: 19px; margin-bottom: 7px; }
  .contact svg { width: 19px; height: 19px; flex: none; }

  .owner-photo {
    position: absolute; left: 720px; top: 0; width: 113px; height: 118px;
    background: linear-gradient(180deg, #c9bfd6 0%, #9c90b0 55%, var(--photo-suit) 100%);
  }
  .house-photo {
    position: absolute; left: 833px; top: 0; width: 115px; height: 118px;
    background: linear-gradient(180deg, #cfc7dc 0%, var(--photo-house) 60%, #9a8fb0 100%);
  }
</style>
</head>
<body>
  <section class="banner" aria-label="Raumglück – Immobilie verkaufen">
    <svg class="banner-band" viewBox="0 0 948 118" preserveAspectRatio="none" aria-hidden="true">
      <polygon points="408,0 948,0 948,118 382,118" fill="var(--brand-lilac)"/>
    </svg>

    <div class="brand">
      <span class="brand-dot"></span>
      <span class="brand-name">RAUM<br>GLÜCK</span>
    </div>

    <h1 class="headline headline-object">IMMOBILIE</h1>
    <h1 class="headline headline-action">VERKAUFEN?</h1>

    <p class="promise">WIR KÜMMERN<br>UNS DARUM.</p>

    <ul class="contact">
      <li>
        <svg viewBox="0 0 20 20" aria-hidden="true">
          <circle cx="10" cy="10" r="10" fill="#fff"/>
          <path d="M7.2 4.6l1.6 2.6-1 1.2c.6 1.5 1.8 2.7 3.3 3.3l1.2-1 2.6 1.6-.6 2.2c-4.6.1-8.6-3.9-8.5-8.5z" fill="var(--brand-lilac)"/>
        </svg>
        <span>02150 – 48 31 706</span>
      </li>
      <li>
        <svg viewBox="0 0 20 20" aria-hidden="true">
          <circle cx="10" cy="10" r="10" fill="#fff"/>
          <g fill="none" stroke="var(--brand-lilac)" stroke-width="1.2">
            <circle cx="10" cy="10" r="5.5"/>
            <ellipse cx="10" cy="10" rx="2.4" ry="5.5"/>
            <line x1="4.5" y1="10" x2="15.5" y2="10"/>
          </g>
        </svg>
        <span>raumglueck.info</span>
      </li>
    </ul>

    <div class="owner-photo" role="img" aria-label="Porträtfoto des Inhabers im dunklen Sakko"></div>
    <div class="house-photo" role="img" aria-label="Foto eines Einfamilienhauses in Lila getönt"></div>
  </section>
</body>
</html>
```